The ONLY 100% Free Security System

We are a national home/auto insurance agency that will be offering home security systems. Our "pitch" is that we will show people (before signing any agreements) how much they can save on their home/auto insurance based on having a security system installed. This is often enough to completely offset the cost of the monthly monitoring fee. One side of the flyer will highlight "The ONLY 100% truly free security system". The other side will list the following bullet points: 1. $100's in FREE Premium Security Equipment 2. FREE Professional Installation 3. "and what no other company offers..." ZERO Cost Monitoring (up to a $74.95 per month value) How? Call our 24-hour message line for a 2-minute overview: (phone # needs to be editable)

The last bullet point (what no other company offers... ZERO cost monitoring) needs to stand out.

Target Market(s)

Homeowners and businesses

Industry/Entity Type

Insurance

Font styles to use
Serif
Sans Serif

Colors

Designer to choose colors to be used in the design.

Requirements
Must have
• Editable phone # - this is also a 5.5"(width) X 8.5" (length) flyer

```html
<!DOCTYPE html>
<html lang="en">
<head>
<meta charset="utf-8">
<title>Shieldwell – Free Security System Flyer</title>
<link href="https://fonts.googleapis.com/css2?family=Fira+Sans+Condensed:wght@500;600;700;800&family=Fira+Sans:wght@400;500;600&display=swap" rel="stylesheet">
<style>
  :root {
    --blue-deep: #1450a0;
    --blue-mid: #1f7cc4;
    --blue-light: #2a9ad8;
    --green: #3aa655;
    --green-dark: #2d8a44;
    --text-blue: #1c4f98;
    --white: #ffffff;
    --backdrop: #e6e6e6;
  }
  * { box-sizing: border-box; margin: 0; padding: 0; }
  html, body { width: 977px; height: 1200px; overflow: hidden; }
  body {
    background: var(--backdrop);
    position: relative;
    font-family: "Fira Sans", Arial, sans-serif;
  }
  .flyer {
    position: absolute;
    top: 267px;
    width: 430px;
    height: 665px;
    background: var(--white);
    overflow: hidden;
    box-shadow: 0 4px 14px rgba(0,0,0,0.18);
  }
  .flyer--front { left: 30px; }
  .flyer--back { left: 517px; }

  .front-bg { position: absolute; inset: 0; }

  .headline {
    position: absolute;
    left: 38px; top: 38px;
    color: var(--white);
    font-family: "Fira Sans Condensed", Arial, sans-serif;
    font-weight: 700;
    line-height: 1;
  }
  .headline span { position: absolute; left: 0; white-space: nowrap; }
  .headline__only { font-size: 27px; top: 0; }
  .headline__pct { font-size: 52px; top: 28px; }
  .headline__free { font-size: 94px; font-weight: 800; left: 140px !important; top: -8px; letter-spacing: 1px; }
  .headline__system { font-size: 45px; top: 80px; letter-spacing: 0.5px; }

  .brand {
    position: absolute;
    left: 0; right: 0;
    display: flex; justify-content: center; align-items: center; gap: 8px;
    font-family: "Fira Sans Condensed", Arial, sans-serif;
    font-weight: 700;
    color: var(--text-blue);
  }
  .brand__dot { width: 12px; height: 12px; border-radius: 50%; background: var(--green); }
  .flyer--front .brand { top: 252px; font-size: 32px; }
  .flyer--back .brand { top: 62px; font-size: 40px; }

  .illustration {
    position: absolute;
    left: 55px; top: 345px;
    width: 320px; height: 240px;
    border-radius: 8px;
    background: radial-gradient(ellipse at 50% 35%, #e8706e 0%, #d9a15a 45%, #f3e9e0 75%, #ffffff 100%);
  }

  .feature-graphic {
    position: absolute;
    left: 72px; top: 135px;
    width: 286px; height: 258px;
    border-radius: 50%;
    background: linear-gradient(135deg, #2aa8e8 0%, #1cc6b4 30%, #c42a9a 60%, #f3582f 100%);
  }

  .contact {
    position: absolute;
    left: 0; right: 0;
    display: flex; justify-content: center; align-items: center; gap: 12px;
    color: var(--text-blue);
  }
  .contact__web { font-size: 13px; font-weight: 600; display: flex; align-items: center; gap: 5px; }
  .contact__divider { width: 1px; height: 20px; background: #999; }
  .contact__phone {
    font-family: "Fira Sans Condensed", Arial, sans-serif;
    font-weight: 600; font-size: 21px; color: var(--green-dark);
    display: flex; align-items: center; gap: 5px;
  }
  .flyer--front .contact { top: 612px; }
  .flyer--back .contact { top: 632px; }
  .rule { position: absolute; left: 0; right: 0; top: 600px; height: 3px; background: var(--blue-deep); }

  .benefits { position: absolute; left: 40px; top: 410px; width: 355px; list-style: none; }
  .benefit { position: relative; height: 44px; margin-bottom: 8px; }
  .benefit__bar {
    position: absolute; left: 18px; right: 0; top: 7px; height: 32px;
    border-radius: 6px;
    background: linear-gradient(180deg, var(--blue-mid), var(--blue-deep));
    color: var(--white);
    font-size: 11.5px; font-weight: 600; line-height: 1.15;
    display: flex; flex-direction: column; justify-content: center; align-items: center;
    padding-left: 28px; text-align: center;
  }
  .benefit__num {
    position: absolute; left: 0; top: 0; width: 44px; height: 44px; border-radius: 50%;
    background: radial-gradient(circle at 40% 35%, #6cc97f, var(--green-dark));
    border: 3px solid var(--white);
    box-shadow: 0 1px 4px rgba(0,0,0,0.25);
    color: var(--white);
    font-size: 24px; font-weight: 500;
    display: flex; align-items: center; justify-content: center;
    z-index: 1;
  }
  .benefit--highlight .benefit__bar { font-size: 12px; }

  .cta {
    position: absolute; left: 0; right: 0; top: 578px; height: 50px;
    background: var(--green);
    color: var(--white); text-align: center;
    padding-top: 6px;
  }
  .cta__title { font-family: "Fira Sans Condensed", Arial, sans-serif; font-weight: 700; font-size: 26px; line-height: 1; }
  .cta__sub { font-size: 12px; font-weight: 500; margin-top: 2px; }
</style>
</head>
<body>

<section class="flyer flyer--front" aria-label="Flyer front">
  <svg class="front-bg" width="430" height="665" viewBox="0 0 430 665" aria-hidden="true">
    <defs>
      <linearGradient id="frontBlue" x1="0" y1="0" x2="0" y2="1">
        <stop offset="0" stop-color="#1450a0"/>
        <stop offset="1" stop-color="#2a9ad8"/>
      </linearGradient>
      <linearGradient id="domeGrey" x1="0" y1="0" x2="0" y2="1">
        <stop offset="0" stop-color="#e9ebee"/>
        <stop offset="0.5" stop-color="#f4f5f6"/>
        <stop offset="1" stop-color="#ffffff"/>
      </linearGradient>
    </defs>
    <rect width="430" height="330" fill="url(#frontBlue)"/>
    <ellipse cx="215" cy="430" rx="250" ry="240" fill="url(#domeGrey)"/>
    <rect y="330" width="430" height="335" fill="#fff" opacity="0.55"/>
  </svg>

  <h1 class="headline">
    <span class="headline__only">THE ONLY</span>
    <span class="headline__pct">100%</span>
    <span class="headline__free">FREE</span>
    <span class="headline__system">SECURITY SYSTEM</span>
  </h1>

  <div class="brand"><span class="brand__dot"></span>Shieldwell</div>

  <div class="illustration" role="img" aria-label="Red umbrella sheltering a house, a red car and a wallet with coins"></div>

  <div class="rule"></div>
  <div class="contact">
    <span class="contact__web">
      <svg width="12" height="12" viewBox="0 0 12 12" aria-hidden="true"><circle cx="6" cy="6" r="5" fill="none" stroke="#3aa655" stroke-width="1.5"/><path d="M1 6h10M6 1c2 2 2 8 0 10M6 1c-2 2-2 8 0 10" fill="none" stroke="#3aa655" stroke-width="1"/></svg>
      www.shieldwellcover.com
    </span>
    <span class="contact__divider"></span>
    <span class="contact__phone">
      <svg width="16" height="16" viewBox="0 0 16 16" aria-hidden="true"><path d="M4 1.5l2.5 3-1.5 1.5c.8 2 2.5 3.7 4.5 4.5l1.5-1.5 3 2.5-1.5 2.5C7 13.5 2.5 9 1.5 3z" fill="#1c4f98"/></svg>
      1200 555 018
    </span>
  </div>
</section>

<section class="flyer flyer--back" aria-label="Flyer back">
  <div class="brand"><span class="brand__dot"></span>Shieldwell</div>

  <div class="feature-graphic" role="img" aria-label="Graphic of three overlapping coloured circles with protection, business and monitoring icons"></div>

  <ol class="benefits">
    <li class="benefit"><span class="benefit__num">1</span><span class="benefit__bar">$100's in FREE Premium Security Equipment</span></li>
    <li class="benefit"><span class="benefit__num">2</span><span class="benefit__bar">FREE Installation<br>And what no other company offers...</span></li>
    <li class="benefit benefit--highlight"><span class="benefit__num">3</span><span class="benefit__bar">ZERO Cost Monitoring<br>(up to a $74.95 per month value)</span></li>
  </ol>

  <div class="cta">
    <div class="cta__title">HOW ARE WE ABLE TO DO THIS?</div>
    <div class="cta__sub">Call our 24-hour message line for a 3-minute overview</div>
  </div>

  <div class="contact">
    <span class="contact__web">
      <svg width="12" height="12" viewBox="0 0 12 12" aria-hidden="true"><circle cx="6" cy="6" r="5" fill="none" stroke="#3aa655" stroke-width="1.5"/><path d="M1 6h10M6 1c2 2 2 8 0 10M6 1c-2 2-2 8 0 10" fill="none" stroke="#3aa655" stroke-width="1"/></svg>
      www.shieldwellcover.com
    </span>
    <span class="contact__divider"></span>
    <span class="contact__phone">
      <svg width="16" height="16" viewBox="0 0 16 16" aria-hidden="true"><path d="M4 1.5l2.5 3-1.5 1.5c.8 2 2.5 3.7 4.5 4.5l1.5-1.5 3 2.5-1.5 2.5C7 13.5 2.5 9 1.5 3z" fill="#1c4f98"/></svg>
      1200 555 018
    </span>
  </div>
</section>

</body>
</html>
```